Contemporary update for a market leader in foodservice distribution

KORVELT is a market leader in foodservice distribution nationwide.
We have recently adopted a new look and feel for our flagship foodservice rewards programme, and we're looking to have our business cards reflect our new aesthetic. Below is a link to our new rewards website to give you a general idea on the look we're after. https://korveltperks.com.au/

Industry/Entity Type

Distribution

Contact Information for Business Card

Must have space for contact name, position, company name and ABN, address, phone number and direct number, fax, email, and web address.

Font styles to use
Serif
Sans Serif

Requirements
Must have
• We'd like a landscape design, with our 'Tip of the Peak' logo incorporated on either the front or the back of the card. The overall design should be contemporary and professional.
Nice to have
• I have included both the full colour and white version of our company logo - our preference is to have the company logo one solid colour (white, or a shade of grey) although we're also open to designs including the full colour logo. If you are able to incorporate a small Facebook and LinkedIn logo, please do so.
Should not have
• Should not have an over-complicated design. No images of globes, or food.

```html
<!DOCTYPE html>
<html lang="en">
<head>
<meta charset="utf-8">
<title>KORVELT Business Card</title>
<link href="https://fonts.googleapis.com/css2?family=Titillium+Web:ital,wght@0,400;0,600;1,400&display=swap" rel="stylesheet">
<style>
  :root {
    --bg: #e4e5e7;
    --card-white: #ffffff;
    --brand-green: #3aaa4a;
    --deep-green: #0f5a26;
    --photo-dark: #0b3a1a;
    --ink: #222222;
    --shadow: rgba(0, 0, 0, 0.18);
  }
  * { box-sizing: border-box; margin: 0; padding: 0; }
  html, body {
    width: 1200px; height: 800px; overflow: hidden;
    background: var(--bg);
    font-family: "Titillium Web", Arial, sans-serif;
  }
  .stage { position: relative; width: 1200px; height: 800px; }
  .card {
    position: absolute; top: 241px;
    width: 520px; height: 318px;
    border-radius: 4px; overflow: hidden;
    box-shadow: 0 10px 24px var(--shadow);
  }
  .card-front { left: 60px; }
  .card-back { left: 620px; background: var(--card-white); }

  /* Front */
  .front-photo {
    position: absolute; inset: 0;
    background: radial-gradient(ellipse at 60% 35%, #36b04f 0%, #1c8a36 40%, var(--photo-dark) 100%);
  }
  .brand-row { display: flex; align-items: center; gap: 14px; }
  .brand-dot { width: 30px; height: 30px; border-radius: 50%; background: currentColor; flex: none; }
  .brand-name {
    font-family: "Titillium Web", Arial, sans-serif;
    font-weight: 400; line-height: 1;
  }
  .front-brand {
    position: absolute; left: 112px; top: 128px;
    color: #fff;
  }
  .front-brand .brand-name { font-size: 56px; letter-spacing: 4px; }

  /* Back */
  .back-brand {
    position: absolute; left: 124px; top: 30px; color: var(--deep-green);
  }
  .back-brand .brand-row { gap: 10px; }
  .back-brand .brand-dot { width: 18px; height: 18px; }
  .back-brand .brand-name { font-size: 36px; letter-spacing: 3px; }
  .name-band {
    position: absolute; left: 0; top: 98px;
    width: 240px; height: 58px;
    background: var(--brand-green); color: #fff;
    padding: 8px 0 0 54px;
  }
  .person-name { font-size: 19px; font-weight: 600; line-height: 1.1; }
  .person-role { font-size: 13px; font-style: italic; opacity: 0.92; }
  .company {
    position: absolute; left: 30px; top: 166px;
    color: var(--ink); font-size: 13px; line-height: 1.3;
  }
  .company-name { font-size: 16px; font-weight: 600; margin-bottom: 2px; }
  .award-seal {
    position: absolute; right: 36px; top: 118px;
    width: 72px; height: 72px; border-radius: 50%;
    background: var(--brand-green);
  }
  .contact-list {
    position: absolute; left: 262px; top: 196px;
    list-style: none; color: var(--ink); font-size: 13.5px;
  }
  .contact-list li { display: flex; align-items: center; gap: 12px; height: 20px; }
  .contact-list svg { width: 15px; height: 15px; flex: none; }
</style>
</head>
<body>
<main class="stage">

  <section class="card card-front">
    <div class="front-photo" role="img" aria-label="Chef cooking with a pan in a commercial kitchen, green duotone photograph"></div>
    <div class="front-brand">
      <div class="brand-row"><span class="brand-dot"></span><span class="brand-name">KORVELT</span></div>
    </div>
  </section>

  <section class="card card-back">
    <div class="back-brand">
      <div class="brand-row"><span class="brand-dot"></span><span class="brand-name">KORVELT</span></div>
    </div>

    <div class="name-band">
      <div class="person-name">Daniel Hartley</div>
      <div class="person-role">Marketing Manager</div>
    </div>

    <div class="company">
      <div class="company-name">Company Name</div>
      <div>ABN: 47 210 583 916</div>
      <div>18 Marlow Street,</div>
      <div>ASHBURY 2193 NSW</div>
    </div>

    <div class="award-seal" role="img" aria-label="Tip of the Peak rewards badge"></div>

    <ul class="contact-list">
      <li>
        <svg viewBox="0 0 16 16" fill="none" stroke="#333" stroke-width="1.3"><rect x="4" y="1" width="8" height="14" rx="1.5"/><line x1="7" y1="12.5" x2="9" y2="12.5"/></svg>
        (02) 9461 3308
      </li>
      <li>
        <svg viewBox="0 0 16 16" fill="none" stroke="#333" stroke-width="1.3"><rect x="2" y="6" width="12" height="8" rx="1"/><rect x="4" y="2" width="8" height="4"/><line x1="5" y1="10" x2="11" y2="10"/></svg>
        (02) 9461 3309
      </li>
      <li>
        <svg viewBox="0 0 16 16" fill="none" stroke="#333" stroke-width="1.3"><rect x="3" y="3" width="10" height="12"/><line x1="5" y1="7" x2="11" y2="7"/><line x1="5" y1="10" x2="11" y2="10"/></svg>
        (02) 9461 3310
      </li>
      <li>
        <svg viewBox="0 0 16 16" fill="none" stroke="#333" stroke-width="1.3"><rect x="1.5" y="3.5" width="13" height="9"/><polyline points="1.5,3.5 8,9 14.5,3.5"/></svg>
        info@korvelt.com
      </li>
      <li>
        <svg viewBox="0 0 16 16" fill="none" stroke="#333" stroke-width="1.3"><rect x="3" y="3" width="10" height="7"/><line x1="1" y1="13" x2="15" y2="13"/></svg>
        korveltperks.com.au
      </li>
    </ul>
  </section>

</main>
</body>
</html>
```